Hot young IT advisor needs business cards as upscale and innovative as they are

We need business cards that make a statement about who we are, as a young and upscale IT advisor. Our whole angle is innovation and tenacity in our personal relationships with our clients. We've just done a brand overhaul and need cards that have the new logos, but we're also looking for someone with a sixth sense who can capture what sets us apart and communicate that with a business card. Clean, minimalist, upscale, innovative, personal. Our budget only allows room for them to be soft-touch, no spot gloss or foil designs please.

Target Market(s)

High-level decision makers at middle-market and large organizations in the healthcare, financial services, sports and entertainment, K-12 education, college and university, state and local government, and federal government sectors.

Industry/Entity Type

Information Technology

Font styles to use
Sans Serif

Colors
ec1f27
606060
ffffff

Requirements
Should not have
• Designs with low contrast which would require spot-gloss or embossing.

```html
<!DOCTYPE html>
<html lang="en">
<head>
<meta charset="utf-8">
<title>Halvern – Business Card</title>
<link href="https://fonts.googleapis.com/css2?family=Open+Sans:wght@400;600&display=swap" rel="stylesheet">
<style>
  :root {
    --brand-red: #e3253f;
    --ink-grey: #606060;
    --paper: #ffffff;
    --backdrop: #2e3033;
    --icon-dark: #333333;
  }
  * { margin: 0; padding: 0; box-sizing: border-box; }
  html, body {
    width: 1200px; height: 900px; overflow: hidden;
    background: var(--backdrop);
    font-family: "Open Sans", Arial, sans-serif;
  }
  .stage { position: relative; width: 1200px; height: 900px; }
  .card {
    position: absolute; left: 260px;
    width: 680px; height: 390px;
    border-radius: 44px; overflow: hidden;
  }
  .card--front { top: 45px; background: var(--brand-red); }
  .card--back { top: 465px; background: var(--paper); display: flex; }

  .brand {
    display: flex; align-items: center; gap: 12px;
    color: var(--paper);
    font-weight: 600; font-size: 30px; letter-spacing: 4px;
    text-transform: uppercase;
  }
  .brand__square { width: 18px; height: 18px; background: var(--paper); }
  .card--front .brand {
    position: absolute; top: 50%; left: 50%;
    transform: translate(-50%, -50%);
  }

  .back__panel {
    width: 300px; height: 100%;
    background: var(--brand-red);
    display: flex; align-items: center; justify-content: center;
  }
  .back__panel .brand { font-size: 24px; letter-spacing: 3px; gap: 10px; }
  .back__panel .brand__square { width: 14px; height: 14px; }

  .back__info { flex: 1; padding: 52px 32px 0 48px; }
  .holder-name {
    font-weight: 400; font-size: 34px; letter-spacing: 1px;
    color: var(--ink-grey); text-transform: uppercase;
    line-height: 1.2;
  }
  .holder-name__accent { color: var(--brand-red); }
  .contact-list { list-style: none; margin-top: 54px; }
  .contact-list li {
    height: 56px; display: flex; align-items: center; gap: 16px;
    font-size: 16px; color: var(--ink-grey); white-space: nowrap;
  }
  .contact-list svg { flex: none; width: 24px; height: 24px; fill: var(--icon-dark); }
</style>
</head>
<body>
<main class="stage">
  <section class="card card--front" aria-label="Card front">
    <div class="brand"><span class="brand__square"></span>Halvern</div>
  </section>

  <section class="card card--back" aria-label="Card back">
    <div class="back__panel">
      <div class="brand"><span class="brand__square"></span>Halvern</div>
    </div>
    <div class="back__info">
      <h1 class="holder-name">Full <span class="holder-name__accent">Name</span></h1>
      <ul class="contact-list">
        <li>
          <svg viewBox="0 0 24 24" aria-hidden="true"><path d="M6.6 10.8a15 15 0 0 0 6.6 6.6l2.2-2.2a1 1 0 0 1 1-.25 11.4 11.4 0 0 0 3.6.57 1 1 0 0 1 1 1V20a1 1 0 0 1-1 1A17 17 0 0 1 3 4a1 1 0 0 1 1-1h3.5a1 1 0 0 1 1 1c0 1.25.2 2.45.57 3.57a1 1 0 0 1-.25 1z"/></svg>
          <span class="contact-list__text">+1 555 0142 388</span>
        </li>
        <li>
          <svg viewBox="0 0 24 24" aria-hidden="true"><path d="M12 2a7 7 0 0 0-7 7c0 5.25 7 13 7 13s7-7.75 7-13a7 7 0 0 0-7-7zm0 9.5A2.5 2.5 0 1 1 12 6.5a2.5 2.5 0 0 1 0 5z"/></svg>
          <span class="contact-list__text">12 Market Street, Springfield</span>
        </li>
        <li>
          <svg viewBox="0 0 24 24" aria-hidden="true"><path d="M2 5h20v14H2z M3.5 6.5 12 13l8.5-6.5" fill="var(--icon-dark)" stroke="#fff" stroke-width="1.2"/></svg>
          <span class="contact-list__text">hello@halvern.com</span>
        </li>
        <li>
          <svg viewBox="0 0 24 24" aria-hidden="true"><circle cx="12" cy="12" r="10"/><g fill="none" stroke="#fff" stroke-width="1.2"><ellipse cx="12" cy="12" rx="4" ry="10"/><path d="M2 12h20M4 7h16M4 17h16M12 2v20"/></g></svg>
          <span class="contact-list__text">www.halvern.com</span>
        </li>
      </ul>
    </div>
  </section>
</main>
</body>
</html>
```